Silver Heron Construction Services

Create a business card for my business consulting company
Danielle Vesk, Founder and CEO
4816 Alder Brook Way, Ste 100
Denver, CO. 80451
303.782.4190 cell
dvesk@silverheronconst.example
www.silverheronconst.example

Target Market(s)

Private Equity and Construction Companies

Industry/Entity Type

Business / Sales Consulting

Contact Information for Business Card

Tag Line that says "Where The Road To Success Is Always Under Construction"

Requirements
Must have
• Logo on both sides of the card.
Nice to have
• Add tagline to the same side of the card as my name and contact info

```html
<!DOCTYPE html>
<html lang="en">
<head>
<meta charset="utf-8">
<title>Silver Heron Construction Services – Business Card</title>
<link href="https://fonts.googleapis.com/css2?family=Montserrat:wght@600;700&family=Lato:wght@400&display=swap" rel="stylesheet">
<style>
  :root {
    --stage: #2b2b2b;
    --card-white: #ffffff;
    --card-black: #141414;
    --ink: #111111;
    --ink-soft: #6d6d6d;
    --rule-grey: #9a9a9a;
    --logo-light: #e6e6e6;
  }
  html, body {
    margin: 0;
    width: 1200px;
    height: 952px;
    overflow: hidden;
    background: var(--stage);
  }
  .canvas {
    position: relative;
    width: 1200px;
    height: 952px;
  }
  .card {
    position: absolute;
    width: 540px;
    height: 310px;
    box-sizing: border-box;
    overflow: hidden;
  }

  /* Front side */
  .card-front {
    left: 50px;
    top: 470px;
    background: var(--card-white);
  }
  .edge-rule-thin {
    position: absolute;
    left: 44px;
    top: 96px;
    width: 2px;
    height: 110px;
    background: var(--rule-grey);
  }
  .edge-rule-thick {
    position: absolute;
    left: 42px;
    top: 206px;
    width: 6px;
    height: 104px;
    background: var(--ink);
  }
  .brand {
    position: absolute;
    display: flex;
    align-items: center;
    gap: 10px;
    font-family: "Montserrat", sans-serif;
    font-weight: 700;
    text-transform: uppercase;
    letter-spacing: 0.5px;
  }
  .brand-mark {
    flex: none;
    width: 16px;
    height: 16px;
  }
  .card-front .brand {
    left: 78px;
    top: 36px;
    width: 230px;
    font-size: 15px;
    line-height: 1.3;
    color: var(--ink);
  }
  .card-front .brand-mark { background: var(--ink); }

  .person {
    position: absolute;
    left: 250px;
    top: 118px;
  }
  .person-name {
    margin: 0;
    font-family: "Montserrat", sans-serif;
    font-weight: 700;
    font-size: 22px;
    letter-spacing: 0.5px;
    text-transform: uppercase;
    color: var(--ink);
  }
  .person-title {
    margin: 2px 0 0;
    font-family: "Lato", sans-serif;
    font-size: 14px;
    color: var(--ink-soft);
  }
  .person-rule {
    width: 52px;
    height: 1px;
    margin-top: 8px;
    background: var(--rule-grey);
  }
  .contact-list {
    list-style: none;
    margin: 14px 0 0;
    padding: 0;
    font-family: "Lato", sans-serif;
    font-size: 12.5px;
    line-height: 1.35;
    color: var(--ink-soft);
  }
  .contact-item {
    display: flex;
    align-items: flex-start;
    gap: 8px;
    margin-bottom: 5px;
  }
  .contact-icon {
    flex: none;
    width: 14px;
    height: 14px;
    margin-top: 1px;
  }

  /* Back side */
  .card-back {
    left: 610px;
    top: 150px;
    background: radial-gradient(ellipse at 55% 45%, #1f1f1f 0%, var(--card-black) 70%);
  }
  .card-back .brand {
    left: 50%;
    top: 50%;
    transform: translate(-50%, -50%);
    width: 260px;
    justify-content: center;
    font-size: 16px;
    line-height: 1.3;
    color: var(--logo-light);
  }
  .card-back .brand-mark { background: var(--logo-light); }
</style>
</head>
<body>
<main class="canvas">

  <section class="card card-back" role="img" aria-label="Card back: black with a subtle diamond lattice texture and the company logo">
    <div class="brand">
      <span class="brand-mark"></span>
      <span class="brand-name">Silver Heron Construction Services</span>
    </div>
  </section>

  <section class="card card-front">
    <div class="edge-rule-thin"></div>
    <div class="edge-rule-thick"></div>

    <div class="brand">
      <span class="brand-mark"></span>
      <span class="brand-name">Silver Heron Construction Services</span>
    </div>

    <div class="person">
      <h1 class="person-name">Danielle Vesk</h1>
      <p class="person-title">Founder and CEO</p>
      <div class="person-rule"></div>

      <ul class="contact-list">
        <li class="contact-item">
          <svg class="contact-icon" viewBox="0 0 14 14" aria-hidden="true">
            <rect width="14" height="14" rx="2" fill="#111"/>
            <path d="M7 2.6a3 3 0 0 0-3 3c0 2.2 3 5.6 3 5.6s3-3.4 3-5.6a3 3 0 0 0-3-3z" fill="#fff"/>
            <circle cx="7" cy="5.6" r="1.1" fill="#111"/>
          </svg>
          <span>4816 Alder Brook Way, Ste 100<br>Denver, CO. 80451</span>
        </li>
        <li class="contact-item">
          <svg class="contact-icon" viewBox="0 0 14 14" aria-hidden="true">
            <rect width="14" height="14" rx="2" fill="#111"/>
            <path d="M4.3 3c.4-.3.9-.2 1.1.2l.8 1.4c.2.4.1.8-.2 1l-.6.5c.5 1 1.3 1.8 2.3 2.3l.5-.6c.3-.3.7-.4 1-.2l1.4.8c.4.2.5.7.2 1.1l-.6.8c-.4.5-1.1.7-1.7.4C6.6 9.8 4.9 8.1 4 6.2c-.3-.6-.1-1.3.3-1.7z" fill="#fff"/>
          </svg>
          <span>+303.782.4190</span>
        </li>
        <li class="contact-item">
          <svg class="contact-icon" viewBox="0 0 14 14" aria-hidden="true">
            <rect width="14" height="14" rx="2" fill="#111"/>
            <rect x="3" y="4.2" width="8" height="5.6" fill="none" stroke="#fff" stroke-width="1"/>
            <path d="M3 4.2l4 3 4-3" fill="none" stroke="#fff" stroke-width="1"/>
          </svg>
          <span>dvesk@silverheronconst.example</span>
        </li>
      </ul>
    </div>
  </section>

</main>
</body>
</html>
```